Thornwell Building Company - advertisement poster

I am looking to print some canvas signs to advertise my general contracting company, Thornwell Building Company. The sign will measure 6' long x 3' high so the size should match that ratio. I already have a logo icon, which is the Letter 'A' and some trees that I would like to incorporate, see attached. I would also like the to have the following information listed:
1) phone number: 472-318-6095
2) email: thornwellbuildingcompany@mailvistra.net
3) website: thornwellbuildingcompany.com
4) Lic#5386204
5) I want to use this text: "BUILD WITH THE T-CREW!"

The ad should be relatively simple and clean. Black and Green are my company colors. I am open to creative ideas!

Target Market(s)

People looking to renovate their homes

Industry/Entity Type

Construction

Colors
59FF00
82FF00
B8FF75
E3FFCB
F4FFEA

Requirements
Must have
• Must have my company logo
Should not have
• No photos or complex graphics

```html
<!DOCTYPE html>
<html lang="en">
<head>
<meta charset="utf-8">
<title>Thornwell Building Company – Poster</title>
<link rel="stylesheet" href="https://fonts.googleapis.com/css2?family=Anton&family=Exo+2:wght@600&family=Source+Sans+3:wght@400;600&display=swap">
<style>
  :root {
    --page-bg: #e9e9e9;
    --poster-black: #231f20;
    --brand-green: #6cb33f;
    --ink-dark: #1f1c1d;
    --text-white: #ffffff;
  }
  * { margin: 0; padding: 0; box-sizing: border-box; }
  html, body {
    width: 1200px; height: 1000px; overflow: hidden;
    background: var(--page-bg);
  }
  .canvas {
    position: relative; width: 1200px; height: 1000px;
  }
  .poster {
    position: absolute; left: 40px; top: 220px;
    width: 1120px; height: 560px;
    background: var(--poster-black);
    overflow: hidden;
  }
  .brand {
    position: absolute; left: 0; right: 0; top: 70px;
    text-align: center;
    font-family: "Exo 2", sans-serif; font-weight: 600;
    color: var(--text-white);
  }
  .brand-dot {
    display: block; width: 22px; height: 22px; margin: 0 auto 18px;
    background: var(--brand-green);
  }
  .brand-name {
    display: block; font-size: 64px; letter-spacing: 2px; line-height: 1;
  }
  .brand-sub {
    display: block; font-size: 22px; letter-spacing: 7px; margin-top: 6px;
  }
  .established {
    position: absolute; top: 120px;
    font-family: "Source Sans 3", sans-serif; font-size: 15px; letter-spacing: 4px;
    color: var(--text-white);
    border-top: 1px solid var(--brand-green);
    border-bottom: 1px solid var(--brand-green);
    padding: 3px 6px;
  }
  .established--left { left: 300px; }
  .established--right { right: 300px; }
  .contact-band {
    position: absolute; left: 0; right: 0; top: 350px; height: 140px;
    background: var(--brand-green);
    clip-path: polygon(0 16px, 100% 0, 100% 100%, 0 100%);
  }
  .headline {
    position: absolute; left: 30px; right: 30px; top: 268px;
    font-family: "Anton", sans-serif; font-size: 100px; line-height: 1;
    color: var(--brand-green); text-align: center; letter-spacing: 1px;
    transform: scaleY(0.92); transform-origin: bottom;
  }
  .phone {
    position: absolute; left: 40px; top: 405px;
    font-family: "Source Sans 3", sans-serif; font-weight: 600;
    font-size: 48px; color: var(--ink-dark);
  }
  .web-contacts {
    position: absolute; left: 455px; top: 395px;
    font-family: "Source Sans 3", sans-serif; font-weight: 400;
    font-size: 28px; line-height: 36px; color: var(--ink-dark);
  }
  .license {
    position: absolute; left: 0; right: 0; top: 502px;
    text-align: center;
    font-family: "Source Sans 3", sans-serif; font-size: 24px;
    color: var(--brand-green);
  }
</style>
</head>
<body>
<main class="canvas">
  <section class="poster">
    <span class="established established--left">ESTD</span>
    <span class="established established--right">2020</span>
    <div class="brand">
      <span class="brand-dot"></span>
      <span class="brand-name">THORNWELL</span>
      <span class="brand-sub">BUILDING COMPANY</span>
    </div>
    <div class="contact-band"></div>
    <h1 class="headline">BUILD WITH THE T-CREW!</h1>
    <p class="phone">472-318-6095</p>
    <p class="web-contacts">thornwellbuildingcompany@mailvistra.net<br>thornwellbuildingcompany.com</p>
    <p class="license">Lic#5386204</p>
  </section>
</main>
</body>
</html>
```